Business card Pfotenweide

Business card is for a self-employed dog trainer with own dog school. Name and logo of the dog school are available. Color specifications as well. The design should be classy and minimalist, but also modern. An already existing idea would be: Front: Only the logo Back: Contact data

Font styles to use
Serif
Sans Serif
Other font styles liked:
• Trajan Pro

Colors
f78f20

Requirements
Must have
• Name: Marlene Kessel-Brand Title: Dipl. Dog Trainer Contain my logo Follow my font and color preferences (see files)

```html
<!DOCTYPE html>
<html lang="de">
<head>
<meta charset="utf-8">
<title>Pfotenweide – Visitenkarte</title>
<link rel="stylesheet" href="https://fonts.googleapis.com/css2?family=Cinzel:wght@400&family=EB+Garamond:wght@400&display=swap">
<style>
  :root {
    --backdrop: #e4e2df;
    --card-white: #ffffff;
    --brand-brown: #7e6757;
    --ink-brown: #6f5848;
    --paper-light: #f6f3ef;
  }
  * { box-sizing: border-box; margin: 0; padding: 0; }
  html, body {
    width: 1200px; height: 873px; overflow: hidden;
    background: var(--backdrop);
  }
  .stage {
    position: relative; width: 1200px; height: 873px;
    display: flex; align-items: center; justify-content: center; gap: 60px;
  }
  .card {
    width: 510px; height: 330px; position: relative;
    box-shadow: 0 2px 10px rgba(0,0,0,0.12);
  }
  /* Contact side */
  .card--contact { background: var(--card-white); }
  .contact-mark {
    position: absolute; left: 52px; top: 112px;
    width: 106px; height: 106px; border-radius: 50%;
    background: var(--brand-brown);
  }
  .contact-divider {
    position: absolute; left: 208px; top: 40px; bottom: 40px;
    width: 1.5px; background: var(--brand-brown);
  }
  .contact-info {
    position: absolute; left: 234px; top: 92px;
    font-family: "EB Garamond", Georgia, serif; color: var(--ink-brown);
  }
  .contact-name { font-size: 25px; line-height: 1.05; }
  .contact-title { font-size: 15px; margin: 2px 0 12px; }
  .contact-list { list-style: none; font-size: 13.5px; line-height: 1.38; }
  .contact-list li { display: flex; align-items: center; gap: 8px; }
  .contact-list svg { width: 11px; height: 11px; flex: none; }
  .contact-list .no-icon { padding-left: 19px; }
  /* Brand side */
  .card--brand {
    background: var(--brand-brown);
    display: flex; flex-direction: column; align-items: center; justify-content: center;
  }
  .brand-circle {
    width: 104px; height: 104px; border-radius: 50%;
    background: var(--paper-light); margin-bottom: 18px;
  }
  .brand-name {
    font-family: "Cinzel", "Times New Roman", serif;
    font-size: 36px; letter-spacing: 0.06em; color: var(--paper-light);
  }
</style>
</head>
<body>
<main class="stage">
  <section class="card card--contact" aria-label="Kontaktseite">
    <div class="contact-mark"></div>
    <div class="contact-divider"></div>
    <div class="contact-info">
      <p class="contact-name">Marlene Kessel-Brand</p>
      <p class="contact-title">Dipl. Hundetrainerin</p>
      <ul class="contact-list">
        <li><svg viewBox="0 0 12 12" fill="none" stroke="currentColor" stroke-width="1"><circle cx="6" cy="6" r="5"/><ellipse cx="6" cy="6" rx="2.2" ry="5"/><line x1="1" y1="6" x2="11" y2="6"/></svg>www.pfotenweide.ch</li>
        <li><svg viewBox="0 0 12 12" fill="currentColor"><path d="M6 1 11 6H9.5V11H2.5V6H1Z"/></svg>Address line</li>
        <li class="no-icon">Zurich, CH 12345</li>
        <li><svg viewBox="0 0 12 12" fill="currentColor"><path d="M3 1l2 2.5-1.2 1.3a6 6 0 0 0 3.4 3.4L8.5 7 11 9l-1.3 1.8C5.5 10.5 1.5 6.5 1.2 2.3Z"/></svg>+01 234 567890</li>
        <li><svg viewBox="0 0 12 12" fill="none" stroke="currentColor" stroke-width="1"><rect x="1" y="2.5" width="10" height="7"/><path d="M1 2.5 6 6.5 11 2.5"/></svg>marlene.kessel-brand@pfotenweide.ch</li>
      </ul>
    </div>
  </section>
  <section class="card card--brand" aria-label="Vorderseite">
    <div class="brand-circle"></div>
    <p class="brand-name">PFOTENWEIDE</p>
  </section>
</main>
</body>
</html>
```